Vorna Fleet business card

I am needing a business card that at a glance shows all the services that we provide emphasizing some more than others. We are a Fleet and Compliance management company as well as a software company. We provide outsourced solutions for KPX compliance and HR services via our own software.
In addition, we do
drug testing
GPS
Cameras
Electronic DVIRS
ELD's

Target Market(s)

Transportation company owners

Industry/Entity Type

Transportation supplier

Contact Information for Business Card

the card should inform potential customers what we do

Other font styles liked:
• I have added brand guidelines. See attached

Requirements
Must have
• See description
Should not have
• Colors outside my brand guide. See attached

```html
<!DOCTYPE html>
<html lang="en">
<head>
<meta charset="utf-8">
<title>Vorna Fleet business card</title>
<link rel="stylesheet" href="https://fonts.googleapis.com/css2?family=Arimo:wght@400;700&display=swap">
<style>
  :root {
    --stage: #222222;
    --brand-red: #ed1c24;
    --ink: #231f20;
    --paper: #ffffff;
    --rule: #555555;
  }
  * { box-sizing: border-box; margin: 0; padding: 0; }
  html, body {
    width: 1200px;
    height: 988px;
    overflow: hidden;
    background: var(--stage);
    font-family: "Arimo", Arial, sans-serif;
  }
  .sheet {
    position: relative;
    width: 1200px;
    height: 988px;
  }
  .card {
    position: absolute;
    width: 560px;
    height: 320px;
    border-radius: 22px;
    overflow: hidden;
  }
  .card--front {
    left: 70px;
    top: 110px;
    background: var(--brand-red);
    color: var(--paper);
  }
  .card--back {
    left: 570px;
    top: 540px;
    background: var(--paper);
    color: var(--ink);
  }

  /* Front */
  .front-brand {
    position: absolute;
    left: 0;
    right: 0;
    top: 108px;
    display: flex;
    justify-content: center;
    align-items: center;
    gap: 14px;
  }
  .brand-mark {
    width: 30px;
    height: 30px;
    background: var(--paper);
    flex: none;
  }
  .front-brand .brand-name {
    font-size: 54px;
    font-weight: 700;
    letter-spacing: 1px;
    color: var(--paper);
    white-space: nowrap;
  }
  .services {
    position: absolute;
    left: 0;
    right: 0;
    bottom: 34px;
    display: flex;
    justify-content: center;
    gap: 16px;
    list-style: none;
    font-size: 14px;
    white-space: nowrap;
  }
  .services li::before {
    content: "\2022";
    margin-right: 5px;
  }

  /* Back */
  .back-brand {
    position: absolute;
    left: 40px;
    top: 140px;
    display: flex;
    align-items: center;
    gap: 12px;
  }
  .back-brand .brand-mark { background: var(--brand-red); width: 24px; height: 24px; }
  .back-brand .brand-name {
    font-size: 38px;
    font-weight: 700;
    color: var(--ink);
    white-space: nowrap;
  }
  .divider {
    position: absolute;
    left: 300px;
    top: 80px;
    width: 1px;
    height: 160px;
    background: var(--rule);
  }
  .contact {
    position: absolute;
    left: 322px;
    top: 78px;
    font-size: 13px;
    line-height: 1.35;
    white-space: nowrap;
  }
  .contact .person {
    font-size: 22px;
    font-weight: 700;
    color: var(--brand-red);
    letter-spacing: 0.5px;
  }
  .contact .role { margin-bottom: 10px; font-size: 14px; }
  .contact .address { margin-bottom: 8px; }
  .contact ul { list-style: none; }
  .contact li { display: flex; align-items: center; gap: 7px; }
  .contact svg { width: 11px; height: 11px; flex: none; }
</style>
</head>
<body>
<main class="sheet">
  <section class="card card--front" aria-label="Card front">
    <div class="front-brand">
      <span class="brand-mark"></span>
      <span class="brand-name">Vorna Fleet</span>
    </div>
    <ul class="services">
      <li>Drug Testing</li>
      <li>GPS</li>
      <li>Cameras</li>
      <li>Electronic DVIRS</li>
      <li>ELD's</li>
    </ul>
  </section>

  <section class="card card--back" aria-label="Card back">
    <div class="back-brand">
      <span class="brand-mark"></span>
      <span class="brand-name">Vorna Fleet</span>
    </div>
    <div class="divider"></div>
    <div class="contact">
      <p class="person">DANA WHITLOW</p>
      <p class="role">CEO/Founder</p>
      <p class="address">1450 W Harlan Avenue<br>Ashford Valley, 7740</p>
      <ul>
        <li>
          <svg viewBox="0 0 12 12" aria-hidden="true"><path fill="#ed1c24" d="M2.5 1l2 2-1 1.3c.7 1.5 1.7 2.5 3.2 3.2L8 6.5l2 2-1.2 1.8C5 10 2 7 1.7 3.2z"/></svg>
          (555) 014-2287
        </li>
        <li>
          <svg viewBox="0 0 12 12" aria-hidden="true"><rect x="1" y="2.5" width="10" height="7" fill="#ed1c24"/><path d="M1 2.5l5 4 5-4" stroke="#fff" fill="none"/></svg>
          info@vornafleet.com
        </li>
        <li>
          <svg viewBox="0 0 12 12" aria-hidden="true"><circle cx="6" cy="6" r="5" fill="#ed1c24"/><path d="M1 6h10M6 1c-2 3-2 7 0 10M6 1c2 3 2 7 0 10" stroke="#fff" stroke-width="0.8" fill="none"/></svg>
          www.vornafleet.com
        </li>
      </ul>
    </div>
  </section>
</main>
</body>
</html>
```